Sliding banner

I need three sliding banners designed for my website tillvane.co.za - please take a look at the existing banner format.

The products items on the banner can be any product that is on the website - the size of the banner must remain the same - the design project is only for the sliding banner.

Regards

```html
<!DOCTYPE html>
<html lang="en">
<head>
<meta charset="utf-8">
<title>Sliding banners</title>
<link rel="stylesheet" href="https://fonts.googleapis.com/css2?family=Ropa+Sans&family=Arimo:wght@400&display=swap">
<style>
  :root {
    --blue-deep: #135d9e;
    --blue-mid: #1f74ba;
    --bar-grey: #d6d6d6;
    --tab-grey: #e4e4e4;
    --tab-arrow: #ffffff;
    --text-white: #ffffff;
    --text-dark: #3a3a3a;
    --btn-light: #f3f5f7;
    --btn-dark: #2b2b2b;
    --btn-blue-text: #1f6fb3;
    --dot-active: #5b8fd6;
    --dot-idle: #b8b8b8;
    --page-bg: #ffffff;
  }
  * { margin: 0; padding: 0; box-sizing: border-box; }
  html, body { width: 1111px; height: 1200px; overflow: hidden; background: var(--page-bg); }
  .stack { width: 1111px; height: 1200px; display: flex; flex-direction: column; gap: 42px; }
  .slider { position: relative; width: 1111px; height: 372px; }
  .slide-stage {
    position: relative; height: 294px; overflow: hidden;
    background:
      radial-gradient(ellipse 60% 80% at 45% 35%, rgba(90,170,230,0.35), transparent 70%),
      linear-gradient(180deg, var(--blue-mid) 0%, var(--blue-deep) 100%);
  }
  .headline {
    position: absolute; left: 112px;
    font-family: "Ropa Sans", sans-serif; color: var(--text-white);
    font-size: 18px; line-height: 25px; white-space: nowrap;
  }
  .headline strong { font-weight: 400; font-size: 22px; }
  .cta {
    position: absolute; height: 40px; padding: 0 11px;
    display: flex; align-items: center; gap: 8px;
    font-family: "Ropa Sans", sans-serif; font-size: 21px; white-space: nowrap;
    box-shadow: 0 2px 4px rgba(0,0,0,0.3);
  }
  .cta--light { background: var(--btn-light); color: var(--btn-blue-text); }
  .cta--dark { background: var(--btn-dark); color: var(--text-white); }
  .cta svg { width: 10px; height: 16px; }
  .product-visual { position: absolute; border-radius: 6px; }
  .nav-tab {
    position: absolute; top: 150px; width: 37px; height: 71px;
    background: var(--tab-grey); display: flex; align-items: center; justify-content: center;
  }
  .nav-tab--prev { left: 0; }
  .nav-tab--next { right: 0; }
  .nav-tab svg { width: 9px; height: 12px; }
  .caption-bar {
    height: 78px; background: var(--bar-grey); position: relative;
    display: flex; align-items: center; justify-content: center;
    font-family: "Arimo", sans-serif; font-size: 15.5px; color: var(--text-dark);
  }
  .dots { position: absolute; right: 20px; top: 42px; display: flex; gap: 10px; }
  .dot { width: 13px; height: 13px; border-radius: 50%; background: var(--dot-idle); }
  .dot--active { background: var(--dot-active); }
</style>
</head>
<body>
<div class="stack">

  <section class="slider">
    <div class="slide-stage">
      <p class="headline" style="top:55px;"><strong>Velo Link</strong> charge/sync cables, now available for your<br>new Velo phone, Velo player or Velo tab.</p>
      <div class="cta cta--light" style="left:428px; top:125px;">GET IT NOW!
        <svg viewBox="0 0 10 16"><path d="M2 2l6 6-6 6" fill="none" stroke="currentColor" stroke-width="2.6"/></svg></div>
      <div class="product-visual" role="img" aria-label="White charge and sync cable with connector and USB plug, coiled at the bottom"
           style="left:732px; top:48px; width:204px; height:246px; background:linear-gradient(180deg, rgba(240,244,248,0.55), rgba(220,230,240,0.25));"></div>
      <div class="nav-tab nav-tab--prev"><svg viewBox="0 0 9 12"><path d="M7 1L2 6l5 5" fill="none" stroke="var(--tab-arrow)" stroke-width="2"/></svg></div>
      <div class="nav-tab nav-tab--next"><svg viewBox="0 0 9 12"><path d="M2 1l5 5-5 5" fill="none" stroke="var(--tab-arrow)" stroke-width="2"/></svg></div>
    </div>
    <div class="caption-bar">Now available in the handy 1m or extra lenght 1.5m Cable
      <div class="dots"><span class="dot dot--active"></span><span class="dot"></span><span class="dot"></span></div>
    </div>
  </section>

  <section class="slider">
    <div class="slide-stage">
      <p class="headline" style="top:58px;"><strong>The Dual USB Car Charger</strong> that lets you juice<br>your mobile devices while on the go.<br>Charge your Mobile phone or Tablet in your car at the same time.</p>
      <div class="cta cta--dark" style="left:444px; top:167px;">GET IT NOW!
        <svg viewBox="0 0 10 16"><path d="M2 2l6 6-6 6" fill="none" stroke="currentColor" stroke-width="2.6"/></svg></div>
      <div class="product-visual" role="img" aria-label="Two white and black dual USB car chargers"
           style="left:660px; top:59px; width:276px; height:239px; background:linear-gradient(160deg, rgba(245,245,245,0.5), rgba(30,30,30,0.35));"></div>
      <div class="nav-tab nav-tab--prev"><svg viewBox="0 0 9 12"><path d="M7 1L2 6l5 5" fill="none" stroke="var(--tab-arrow)" stroke-width="2"/></svg></div>
      <div class="nav-tab nav-tab--next"><svg viewBox="0 0 9 12"><path d="M2 1l5 5-5 5" fill="none" stroke="var(--tab-arrow)" stroke-width="2"/></svg></div>
    </div>
    <div class="caption-bar">High Output 5v - 2amps - Fully charged in no time
      <div class="dots"><span class="dot dot--active"></span><span class="dot"></span><span class="dot"></span></div>
    </div>
  </section>

  <section class="slider">
    <div class="slide-stage">
      <p class="headline" style="top:58px;"><strong>Rechargeable</strong> battery for powering up your<br>Mobile phone or Tablet when you can't find a power outlet.</p>
      <div class="cta cta--light" style="left:396px; top:137px;">GET IT NOW!
        <svg viewBox="0 0 10 16"><path d="M2 2l6 6-6 6" fill="none" stroke="currentColor" stroke-width="2.6"/></svg></div>
      <div class="product-visual" role="img" aria-label="Tablet charging from a grey portable battery pack via a white cable"
           style="left:652px; top:89px; width:296px; height:205px; background:linear-gradient(150deg, rgba(30,30,30,0.45), rgba(150,155,160,0.4));"></div>
      <div class="nav-tab nav-tab--prev"><svg viewBox="0 0 9 12"><path d="M7 1L2 6l5 5" fill="none" stroke="var(--tab-arrow)" stroke-width="2"/></svg></div>
      <div class="nav-tab nav-tab--next"><svg viewBox="0 0 9 12"><path d="M2 1l5 5-5 5" fill="none" stroke="var(--tab-arrow)" stroke-width="2"/></svg></div>
    </div>
    <div class="caption-bar">Great for travelling, power outages, emergencies or other occasions
      <div class="dots"><span class="dot dot--active"></span><span class="dot"></span><span class="dot"></span></div>
    </div>
  </section>

</div>
</body>
</html>
```